Company Real Estate Site Needs A Face Lift

I need a new website for the recent company I formed: Corvel Real Estate.
You can use my agent website WWW.PALTUNE.COM to see the style/brand I already have. I will have areas for Searching for homes on QRV, etc.
I really like this site:
http://www.amberfieldhomestead.example/
I have attached my logo as well

Industry/Entity Type

Real Estate

Colors
0255a3
ffffff
cee9f5

```html
<!DOCTYPE html>
<html lang="en">
<head>
<meta charset="utf-8">
<title>Corvel Real Estate</title>
<link rel="stylesheet" href="https://fonts.googleapis.com/css2?family=Ubuntu:wght@400;500;700&family=Barlow+Semi+Condensed:wght@600;700&family=Roboto+Condensed:wght@700&display=swap">
<style>
:root{
  --brand:#0255a3;
  --white:#ffffff;
  --ice:#cee9f5;
  --ice-glass:rgba(206,233,245,.78);
  --hero-glass:rgba(38,96,160,.55);
  --ink:#0b2f5c;
  --link:#1560ad;
}
*{margin:0;padding:0;box-sizing:border-box}
html,body{width:1200px;height:883px;overflow:hidden;background:var(--white)}
.page{position:relative;width:1200px;height:883px;overflow:hidden;font-family:"Ubuntu",sans-serif}
.backdrop{position:absolute;inset:0;background:
  radial-gradient(ellipse at 70% 45%,#6d7f92 0%,transparent 45%),
  linear-gradient(180deg,#c7ccd0 0%,#aeb6bd 35%,#8e98a2 60%,#b9c2c9 100%)}
.slant{position:absolute;inset:0}
.masthead{position:absolute;left:0;top:0;width:1200px;height:100px}
.brand{position:absolute;left:20px;top:40px;color:var(--brand);font-weight:700;font-size:30px;letter-spacing:1px;display:flex;align-items:center;gap:8px}
.brand .dot{width:14px;height:14px;border-radius:50%;background:var(--brand)}
.brand small{position:absolute;left:22px;top:40px;font-size:12px;letter-spacing:4px;font-weight:700;color:var(--brand);white-space:nowrap}
.utility{position:absolute;top:16px;left:733px;display:flex;align-items:center;gap:16px;font-size:11px;color:var(--link)}
.utility .icon{display:inline-block;width:14px;height:10px;border:1.5px solid var(--link);margin-right:5px;vertical-align:-1px}
.utility .sales{font-size:15px;font-weight:500;color:var(--brand);margin-left:4px}
.nav{position:absolute;top:57px;left:268px;display:flex;list-style:none;font-size:14px;font-weight:500;color:var(--brand)}
.nav li{height:22px;line-height:22px;margin-right:39px}
.nav li.active{background:var(--brand);color:var(--white);width:100px;text-align:center;clip-path:polygon(8px 0,100% 0,92px 100%,0 100%);margin-right:36px}
.hero{position:absolute;left:458px;top:182px;width:683px;height:414px;background:var(--hero-glass);color:var(--white);padding:0 42px}
.hero h1{font-family:"Barlow Semi Condensed",sans-serif;font-weight:700;font-size:54px;margin-top:2px;letter-spacing:.5px}
.hero .phone{font-family:"Barlow Semi Condensed",sans-serif;font-weight:600;font-size:27px;margin-top:-4px}
.hero .email{font-family:"Barlow Semi Condensed",sans-serif;font-weight:600;font-size:21px;margin-top:12px}
.hero p{font-family:"Roboto Condensed",sans-serif;font-weight:700;font-size:12px;line-height:26.5px;margin-top:18px;width:592px}
.hero .trailer{position:absolute;right:58px;top:316px;font-family:"Roboto Condensed",sans-serif;font-weight:700;font-size:17px}
.footer{position:absolute;left:0;top:620px;width:1200px;height:263px;background:var(--ice-glass)}
.col{position:absolute;top:16px}
.col h3{font-size:15px;font-weight:500;color:var(--ink)}
.col h3::after{content:"";display:inline-block;width:7px;height:7px;border-right:1.5px solid var(--ink);border-bottom:1.5px solid var(--ink);transform:rotate(45deg);margin-left:8px;vertical-align:3px}
.col p,.col li{font-size:11px;color:var(--link);font-weight:500}
.col ul{list-style:none;margin-top:18px}
.col ul li{margin-bottom:13px}
.col .blurb{margin-top:16px;width:186px;text-align:justify;line-height:15.5px}
.contact-tag{display:inline-block;margin:14px 0 8px;background:var(--brand);color:var(--white);font-size:11px;font-weight:700;width:96px;height:19px;line-height:19px;text-align:center;clip-path:polygon(6px 0,100% 0,90px 100%,0 100%)}
.follow{display:inline-block;margin-top:12px;background:var(--white);border-radius:3px;padding:2px 8px;font-size:10px;color:var(--ink);font-weight:700}
.follow::before{content:"";display:inline-block;width:8px;height:8px;border-radius:50%;background:#4aa5e0;margin-right:5px}
.more{position:absolute;left:689px;top:128px;font-size:11px;color:var(--link);font-weight:500}
.to-top{position:absolute;left:1052px;top:139px;width:18px;height:18px;background:var(--brand)}
.rule{position:absolute;left:117px;top:157px;width:953px;height:1px;background:var(--ink)}
.footnav{position:absolute;top:175px;left:129px;display:flex;list-style:none;font-size:14px;color:var(--link)}
.footnav li{margin-right:38px}
.copy{position:absolute;top:204px;left:0;width:1096px;text-align:center;font-size:14px;color:var(--link)}
.social{position:absolute;left:946px;top:187px;display:flex;gap:3px}
.social span{width:29px;height:29px;border-radius:4px}
</style>
</head>
<body>
<div class="page">
  <div class="backdrop" role="img" aria-label="Photo of a bright modern living room with a white fireplace wall, tall bookshelves and white lounge chairs"></div>
  <svg class="slant" width="1200" height="883" aria-hidden="true">
    <polygon points="0,0 225,0 190,100 0,620" fill="#cee9f5" fill-opacity=".75"/>
    <polygon points="190,100 1200,100 1200,0 225,0" fill="#cee9f5" fill-opacity=".85"/>
  </svg>

  <header class="masthead">
    <div class="brand"><span class="dot"></span>Corvel<small>REAL ESTATE</small></div>
    <div class="utility">
      <span><i class="icon"></i>NEWS</span>
      <span><i class="icon" style="width:11px;height:11px;transform:rotate(45deg)"></i>GALLERIES</span>
      <span class="sales">Sales 888.555.0142</span>
    </div>
    <ul class="nav">
      <li class="active">Home</li><li>Search Homes</li><li>Buy</li><li>Sell</li><li>Tours</li><li>Testimonials</li><li>Home Blog</li><li>Contact Us</li>
    </ul>
  </header>

  <section class="hero">
    <h1>DANE HOLLIS</h1>
    <div class="phone">555-638-0127</div>
    <div class="email">DaneHollis@corvelmail.example</div>
    <p>Whether you are a first time buyer, or a home buying expert, finding and purchasing your West Virginia dream home can be an overwhelming process. If you want to avoid the pitfalls and aggravation often accompanied with buying or selling a home, it may be in your best interest to work with a licensed agent. If you are considering buying or selling a home and would like to speak to a Charleston area Real Estate professional, call DANE HOLLIS 555-NET-DANE (638-0127) or email danehollis@corvelmail.example today.</p>
    <div class="trailer">VIEW THE TRAILER</div>
  </section>

  <footer class="footer">
    <div class="col" style="left:119px">
      <h3>Corvel</h3>
      <p style="margin-top:12px">Contact our sales team today.</p>
      <div class="contact-tag">CONTACTUS</div>
      <p>555-776-0153</p>
      <p style="margin-top:3px">555-776-0163</p>
    </div>
    <div class="col" style="left:340px">
      <h3>Latest Updates</h3>
      <ul><li>Happening</li><li>Residence</li><li>News</li></ul>
    </div>
    <div class="col" style="left:606px">
      <h3>On Socialbook</h3>
      <p class="blurb">Lorem ipsum dolor sit amet, consectetuer adipiscing elit, sed diam nonummy nibh euismod tincidunt ut laoreet dolore</p>
    </div>
    <div class="more">visit on socialbook ....</div>
    <div class="col" style="left:885px">
      <h3>On Chirper</h3>
      <p class="blurb">Lorem ipsum dolor sit amet, consectetuer adipiscing elit, sed diam nonummy nibh euismod tincidunt ut laoreet dolore</p>
      <span class="follow">Follow @corvel</span>
    </div>
    <svg class="to-top" viewBox="0 0 18 18" aria-label="Back to top"><path d="M5 11 L9 7 L13 11" stroke="#fff" stroke-width="1.5" fill="none"/></svg>
    <div class="rule"></div>
    <ul class="footnav">
      <li>Home</li><li>Search Homes</li><li>Buy</li><li>Sell</li><li>Tours</li><li>Testimonials</li><li>Home Blog</li><li>Contact Us</li>
    </ul>
    <div class="copy">Copyright © Corvel. All Rights Reserved.</div>
    <div class="social">
      <span style="background:#3b5b99"></span><span style="background:#2fa6df"></span><span style="background:#c4302b"></span><span style="background:#f08a24"></span>
    </div>
  </footer>
</div>
</body>
</html>
```